Taomeng business card -we import and distributed Chinese herbal medicine into Australia for prac...

We need a business card for our recently purchased and rebranded company. We are a small family run business - husband and wife team. Our logo is red and black, and we would like the card to be white, with an element of gold in the design (the first cloud in the attached png) which when printed we would like embossed in gold. Our website uses Chinese water colour paintings in the banners (www.taomeng.net.au) so a design that is in harmony with this would be ideal.
side one needs to include:

Target Market(s)

potential customers

Industry/Entity Type

Health And Wellness

Contact Information for Business Card

Side 1
logo,
Edmund Varsk Director
Practitioner Support and Education
0491 722 413
edmund@taomeng.net.au
218 Colbury St, Kelmsbury, KV, 7714

side 2 needs to include:
logo
Priscilla Moult Director
Orders, Accounts and Despatch
0487 530 619
priscilla@taomeng.net.au

Font styles to use
Serif

Colors

Designer to choose colors to be used in the design.

Requirements
Must have
• black, red, gold colours
Nice to have
• we like the font papyrus (mac font)

```html
<!DOCTYPE html>
<html lang="en">
<head>
<meta charset="utf-8">
<title>Taomeng Business Cards</title>
<link href="https://fonts.googleapis.com/css2?family=Josefin+Sans:wght@300;400&display=swap" rel="stylesheet">
<style>
  :root {
    --page-bg: #d9d9d9;
    --ink-deep: #161c28;
    --ink-mid: #26324a;
    --ink-light: #3a4a66;
    --text-light: #f2f2f2;
    --accent-red: #e3202c;
    --gold: #f2c14e;
    --gold-deep: #e0a92e;
  }
  * { box-sizing: border-box; margin: 0; padding: 0; }
  html, body {
    width: 1200px; height: 1200px; overflow: hidden;
    background: var(--page-bg);
    font-family: "Josefin Sans", sans-serif;
  }
  .sheet {
    width: 1200px; height: 1200px;
    display: flex; flex-direction: column;
    align-items: center; justify-content: center; gap: 56px;
  }
  .card {
    position: relative;
    width: 880px; height: 503px;
    overflow: hidden;
    background:
      radial-gradient(ellipse 60% 55% at 35% 60%, var(--ink-deep) 0%, rgba(22,28,40,0.6) 55%, transparent 80%),
      radial-gradient(ellipse 50% 40% at 80% 20%, var(--ink-light) 0%, transparent 70%),
      linear-gradient(160deg, var(--ink-light) 0%, var(--ink-mid) 45%, var(--ink-deep) 100%);
    color: var(--text-light);
    box-shadow: 0 14px 30px rgba(0,0,0,0.22);
  }
  .brand {
    position: absolute; top: 44px; right: 60px;
    display: flex; align-items: center; gap: 14px;
  }
  .brand-square { width: 34px; height: 58px; background: var(--accent-red); }
  .brand-name {
    font-size: 40px; font-weight: 400; letter-spacing: 2px;
    line-height: 1; color: var(--text-light); text-transform: uppercase;
  }
  .cloud-emboss {
    position: absolute; right: 40px; top: 190px;
    width: 280px; height: 140px;
    border-radius: 70px 90px 60px 80px;
    background: radial-gradient(ellipse at 40% 50%, var(--gold) 0%, var(--gold-deep) 100%);
  }
  .contact-list {
    position: absolute; left: 58px; top: 112px;
    list-style: none; display: flex; flex-direction: column; gap: 12px;
  }
  .contact-item {
    display: flex; align-items: center; gap: 16px;
    font-size: 22px; font-weight: 300; letter-spacing: 0.3px;
    white-space: nowrap;
  }
  .icon {
    width: 34px; height: 34px; border-radius: 50%;
    background: var(--accent-red);
    display: flex; align-items: center; justify-content: center; flex: none;
  }
  .icon svg { width: 18px; height: 18px; }
  .person { position: absolute; left: 58px; bottom: 48px; }
  .role { color: var(--accent-red); font-size: 19px; font-weight: 300; line-height: 1.2; margin-bottom: 4px; }
  .person-name { font-size: 48px; font-weight: 400; letter-spacing: 0.5px; line-height: 1.1; white-space: nowrap; }
  .duty { color: var(--accent-red); font-size: 21px; font-weight: 300; letter-spacing: 0.6px; line-height: 1.2; margin-top: 6px; white-space: nowrap; }
</style>
</head>
<body>
<main class="sheet">

  <section class="card card--priscilla">
    <div class="brand">
      <span class="brand-square"></span>
      <span class="brand-name">Taomeng</span>
    </div>
    <div class="cloud-emboss" role="img" aria-label="Gold embossed Chinese auspicious cloud ornament"></div>
    <ul class="contact-list">
      <li class="contact-item">
        <span class="icon"><svg viewBox="0 0 24 24"><path fill="#fff" d="M12 2a7 7 0 0 0-7 7c0 5 7 13 7 13s7-8 7-13a7 7 0 0 0-7-7zm0 9.5a2.5 2.5 0 1 1 0-5 2.5 2.5 0 0 1 0 5z"/></svg></span>
        218 Colbury St, Kelmsbury, KV, 7714
      </li>
      <li class="contact-item">
        <span class="icon"><svg viewBox="0 0 24 24"><path fill="#fff" d="M6.6 10.8a15 15 0 0 0 6.6 6.6l2.2-2.2c.3-.3.7-.4 1-.2 1.1.4 2.3.6 3.6.6.6 0 1 .4 1 1V20c0 .6-.4 1-1 1A17 17 0 0 1 3 4c0-.6.4-1 1-1h3.5c.6 0 1 .4 1 1 0 1.3.2 2.5.6 3.6.1.3 0 .7-.2 1z"/></svg></span>
        0487 530 619
      </li>
      <li class="contact-item">
        <span class="icon"><svg viewBox="0 0 24 24"><path fill="#fff" d="M3 5h18v14H3z"/><path fill="none" stroke="#e3202c" stroke-width="1.6" d="M3 5l9 7 9-7"/></svg></span>
        priscilla@taomeng.net.au
      </li>
      <li class="contact-item">
        <span class="icon"><svg viewBox="0 0 24 24" fill="none" stroke="#fff" stroke-width="1.8"><circle cx="12" cy="12" r="9"/><ellipse cx="12" cy="12" rx="4" ry="9"/><path d="M3 12h18"/></svg></span>
        www.taomeng.net.au
      </li>
    </ul>
    <div class="person">
      <p class="role">Director</p>
      <h2 class="person-name">Priscilla Moult</h2>
      <p class="duty">Orders, Accounts and Despatch</p>
    </div>
  </section>

  <section class="card card--edmund">
    <div class="brand">
      <span class="brand-square"></span>
      <span class="brand-name">Taomeng</span>
    </div>
    <div class="cloud-emboss" role="img" aria-label="Gold embossed Chinese auspicious cloud ornament"></div>
    <ul class="contact-list">
      <li class="contact-item">
        <span class="icon"><svg viewBox="0 0 24 24"><path fill="#fff" d="M12 2a7 7 0 0 0-7 7c0 5 7 13 7 13s7-8 7-13a7 7 0 0 0-7-7zm0 9.5a2.5 2.5 0 1 1 0-5 2.5 2.5 0 0 1 0 5z"/></svg></span>
        218 Colbury St, Kelmsbury, KV, 7714
      </li>
      <li class="contact-item">
        <span class="icon"><svg viewBox="0 0 24 24"><path fill="#fff" d="M6.6 10.8a15 15 0 0 0 6.6 6.6l2.2-2.2c.3-.3.7-.4 1-.2 1.1.4 2.3.6 3.6.6.6 0 1 .4 1 1V20c0 .6-.4 1-1 1A17 17 0 0 1 3 4c0-.6.4-1 1-1h3.5c.6 0 1 .4 1 1 0 1.3.2 2.5.6 3.6.1.3 0 .7-.2 1z"/></svg></span>
        0491 722 413
      </li>
      <li class="contact-item">
        <span class="icon"><svg viewBox="0 0 24 24"><path fill="#fff" d="M3 5h18v14H3z"/><path fill="none" stroke="#e3202c" stroke-width="1.6" d="M3 5l9 7 9-7"/></svg></span>
        edmund@taomeng.net.au
      </li>
      <li class="contact-item">
        <span class="icon"><svg viewBox="0 0 24 24" fill="none" stroke="#fff" stroke-width="1.8"><circle cx="12" cy="12" r="9"/><ellipse cx="12" cy="12" rx="4" ry="9"/><path d="M3 12h18"/></svg></span>
        www.taomeng.net.au
      </li>
    </ul>
    <div class="person">
      <p class="role">Director</p>
      <h2 class="person-name">Edmund Varsk</h2>
      <p class="duty">Practitioner Support &amp; Education</p>
    </div>
  </section>

</main>
</body>
</html>
```